Robotic Physical Therapy office needs a Grand Opening Flyer

We need a Grand Opening flyer design for a robotic physical therapy office named Stellar Motion Therapy. We would like it to have a clean, classy, upscale feeling that gives potential clients a V.I.P. feeling. We would like to use the colors black, gray, and yellow (logo will be uploaded).

Event: Thursday, June 1st, 2023 from 12pm-6pm
location: 58274 Harlow Ave, Bloomfield Hills, MI 48319

Industry/Entity Type

Physical therapy

Font styles to use
Script

Colors

Designer to choose colors to be used in the design.

Requirements
Nice to have
• More of a vip feel for the invite

```html
<!DOCTYPE html>
<html lang="en">
<head>
<meta charset="utf-8">
<title>Stellar Motion Therapy – Grand Opening Ceremony</title>
<link rel="stylesheet" href="https://fonts.googleapis.com/css2?family=Montserrat:wght@500;600;700;800&family=Satisfy&display=swap">
<style>
  :root{
    --stage:#c8c8c8;
    --ink:#1f1f1f;
    --charcoal:#2a2d33;
    --ring:#555b5c;
    --gold:#fbbd2b;
    --gold-deep:#f5a623;
    --gold-light:#fdd25a;
    --white:#ffffff;
    --sky-1:#eaf4fa;
    --sky-2:#c4dbe8;
    --sky-3:#9fbfd2;
  }
  *{box-sizing:border-box;margin:0;padding:0}
  html,body{width:1200px;height:2263px;overflow:hidden;background:var(--stage)}
  .canvas{position:relative;width:1200px;height:2263px}
  .flyer{
    position:absolute;left:80px;top:396px;width:1040px;height:1470px;overflow:hidden;
    background:radial-gradient(ellipse at 70% 20%,var(--sky-1) 0%,var(--sky-2) 55%,var(--sky-3) 100%);
    box-shadow:-14px 12px 24px rgba(0,0,0,.25);
    font-family:"Montserrat",sans-serif;color:var(--ink);
  }
  .flyer__backdrop{position:absolute;inset:0}
  .flyer__shapes{position:absolute;left:0;top:0;width:1040px;height:1470px}
  .brand{position:absolute;left:0;right:0;top:60px;display:flex;justify-content:center;align-items:center;gap:22px}
  .brand__dot{width:110px;height:110px;border-radius:50%;background:var(--charcoal)}
  .brand__name{font-weight:700;font-size:46px;line-height:1.05;color:var(--charcoal);letter-spacing:.5px}
  .headline{position:absolute;left:0;right:0;text-align:center;font-weight:800;color:var(--ink);letter-spacing:3px;line-height:1}
  .headline--grand{top:245px;font-size:104px}
  .headline--opening{top:352px;font-size:112px}
  .script{font-family:"Satisfy",cursive;color:var(--gold);font-weight:400}
  .ceremony{position:absolute;left:410px;top:395px;font-size:128px;line-height:1}
  .tagline{
    position:absolute;left:243px;top:517px;width:554px;height:63px;border-radius:32px;
    background:var(--charcoal);color:var(--white);font-weight:600;font-size:36px;
    display:flex;align-items:center;justify-content:center;letter-spacing:.5px
  }
  .photo{
    position:absolute;left:43px;top:610px;width:480px;height:480px;border-radius:50%;
    border:12px solid var(--ring);
    background:linear-gradient(160deg,#f4f6f7 0%,#dfe5e8 45%,#9aa3a8 70%,#6d9bc3 100%)
  }
  .event{position:absolute;left:0;right:0;text-align:center;color:var(--white)}
  .event__label{top:1060px;font-size:84px;line-height:1;padding-left:-20px}
  .event__date{top:1162px;font-size:50px;font-weight:800;letter-spacing:1px}
  .event__date .sep{font-weight:500;margin:0 6px}
  .event__time{
    position:absolute;left:343px;top:1232px;width:355px;height:63px;border-radius:32px;
    background:var(--gold);color:var(--ink);display:flex;align-items:center;justify-content:center;gap:10px;
    font-weight:600;font-size:42px
  }
  .event__time .from{font-family:"Satisfy",cursive;font-size:32px;font-weight:400}
  .event__heading{top:1322px;font-size:36px;font-weight:700;color:var(--gold);letter-spacing:1px}
  .event__address{top:1377px;font-size:31px;font-weight:500}
</style>
</head>
<body>
<main class="canvas">
  <article class="flyer">
    <div class="flyer__backdrop" role="img" aria-label="Soft blurred bright clinic interior in pale blue and white tones"></div>

    <svg class="flyer__shapes" viewBox="0 0 1040 1470" aria-hidden="true">
      <path fill="var(--gold)" d="M0,920 C230,890 370,720 560,722 C690,724 770,790 860,772 C900,760 890,705 845,665 C910,640 980,628 1040,618 L1040,740 C980,748 940,765 890,792 C800,860 690,848 520,866 C350,884 200,1010 0,1045 Z"/>
      <path fill="var(--gold-deep)" d="M845,665 C890,705 900,760 860,772 L890,792 C940,765 980,748 1040,740 L1040,700 C980,705 920,700 845,665 Z" opacity=".6"/>
      <path fill="var(--ink)" d="M0,1045 C200,1010 350,884 520,866 C690,848 800,860 890,792 C940,765 980,748 1040,740 L1040,1470 L0,1470 Z"/>
    </svg>

    <header class="brand">
      <span class="brand__dot"></span>
      <span class="brand__name">Stellar Motion<br>Therapy</span>
    </header>

    <h1 class="headline headline--grand">GRAND</h1>
    <h1 class="headline headline--opening">OPENING</h1>
    <span class="script ceremony">Ceremony</span>
    <p class="tagline">Robotic Physical Therapy</p>

    <div class="photo" role="img" aria-label="Photo of a therapist assisting a patient on a robotic therapy machine"></div>

    <p class="event event__label script">Event</p>
    <p class="event event__date">JUNE 1ST, 2023<span class="sep">|</span>THURSDAY</p>
    <p class="event__time"><span class="from">from</span> 12pm-6pm</p>
    <p class="event event__heading">LOCATION</p>
    <p class="event event__address">58274 Harlow Ave, Bloomfield Hills, MI 48319</p>
  </article>
</main>
</body>
</html>
```